Telecommunications/Power civil contractor needs business card design

Were a new telecommunications/power underground civil contractor that is looking for a new business card design. Our company colours are silver or grey and orange. Feel free to use the white background logo or the black background logo.

Target Market(s)

Local contractors, utility companies, private sector mining/energy companies, developers.

Industry/Entity Type

Telecommunications

Contact Information for Business Card

Each card will need the following info:
Persons name:
Title:
E-mail:
Phone number:
Shop Address:
Mailing Address:

Requirements
Must have
• Each card will need the following info:
• Persons name:
• Title:
• E-mail:
• Phone number:
• Shop Address:
• Mailing Address:

```html
<!DOCTYPE html>
<html lang="en">
<head>
<meta charset="utf-8">
<title>Ridgeline Civil Inc — Business Card</title>
<link href="https://fonts.googleapis.com/css2?family=Arimo:wght@400;700&display=swap" rel="stylesheet">
<style>
  :root {
    --backdrop: #2b2b2b;
    --card: #f4f4f4;
    --orange: #d9531e;
    --grey: #6b6b6b;
    --ink: #4a4a4a;
    --ink-soft: #5c5c5c;
  }
  html, body {
    margin: 0;
    width: 1200px;
    height: 997px;
    overflow: hidden;
    background: var(--backdrop);
    font-family: "Arimo", Arial, sans-serif;
  }
  .card {
    position: absolute;
    left: 150px;
    top: 241px;
    width: 900px;
    height: 514px;
    border-radius: 24px;
    background: linear-gradient(135deg, #ffffff 0%, var(--card) 60%, #e6e6e6 100%);
    overflow: hidden;
    box-shadow: 0 18px 40px rgba(0,0,0,.45);
  }
  .card__swoosh {
    position: absolute;
    inset: 0;
    width: 900px;
    height: 514px;
  }
  .person {
    position: absolute;
    left: 62px;
    top: 70px;
    color: var(--ink);
  }
  .person__name {
    font-size: 30px;
    font-weight: 700;
    font-variant: small-caps;
    letter-spacing: 1px;
    margin: 0;
  }
  .person__title {
    font-size: 21px;
    margin: 2px 0 14px;
    color: var(--ink-soft);
  }
  .person__email {
    font-size: 21px;
    color: var(--orange);
    font-style: italic;
  }
  .contact {
    position: absolute;
    left: 62px;
    top: 222px;
    list-style: none;
    margin: 0;
    padding: 0;
    color: var(--ink-soft);
    font-size: 20px;
    line-height: 30px;
  }
  .contact__item {
    display: flex;
    align-items: flex-start;
    gap: 16px;
  }
  .contact__icon {
    flex: none;
    width: 20px;
    height: 20px;
    margin-top: 5px;
  }
  .brand {
    position: absolute;
    right: 58px;
    top: 118px;
    display: flex;
    flex-direction: column;
    align-items: flex-end;
    gap: 14px;
  }
  .brand__mark {
    width: 96px;
    height: 96px;
    border-radius: 50%;
    border: 8px solid var(--grey);
    box-sizing: border-box;
    background: #fff;
  }
  .brand__name {
    font-size: 34px;
    font-weight: 700;
    color: var(--grey);
    letter-spacing: 1px;
    text-align: right;
    line-height: 1;
  }
</style>
</head>
<body>
  <article class="card">
    <svg class="card__swoosh" viewBox="0 0 900 514" aria-hidden="true">
      <path fill="#6b6b6b" d="M0,408 C270,420 450,370 590,250 C620,225 640,215 662,210 C650,226 630,242 612,262 C470,400 280,456 0,452 Z"/>
      <path fill="#d9531e" d="M0,375 C250,390 420,340 560,220 C640,150 760,150 900,170 L900,180 C770,164 650,168 575,238 C440,362 260,410 0,402 Z"/>
    </svg>

    <header class="person">
      <h1 class="person__name">Marcus T Bell</h1>
      <p class="person__title">Managing Partner</p>
      <span class="person__email">marcus@ridgelinecivilinc.com</span>
    </header>

    <ul class="contact">
      <li class="contact__item">
        <svg class="contact__icon" viewBox="0 0 20 20" aria-label="Phone"><rect width="20" height="20" rx="4" fill="#6b6b6b"/><path d="M6 5h3l1 3-2 1a7 7 0 0 0 3 3l1-2 3 1v3a1 1 0 0 1-1 1A10 10 0 0 1 5 6a1 1 0 0 1 1-1z" fill="#fff"/></svg>
        <span>+1 (555) 214-3380</span>
      </li>
      <li class="contact__item">
        <svg class="contact__icon" viewBox="0 0 20 20" aria-label="Shop address"><rect width="20" height="20" rx="4" fill="#6b6b6b"/><path d="M10 4 4 9h2v6h3v-4h2v4h3V9h2z" fill="#fff"/></svg>
        <span>Shop no 42, Unit 7, Dover</span>
      </li>
      <li class="contact__item">
        <svg class="contact__icon" viewBox="0 0 20 20" aria-label="Mailing address"><rect width="20" height="20" rx="4" fill="#6b6b6b"/><path d="M10 4a4 4 0 0 0-4 4c0 3 4 8 4 8s4-5 4-8a4 4 0 0 0-4-4zm0 5.5A1.5 1.5 0 1 1 10 6.5a1.5 1.5 0 0 1 0 3z" fill="#fff"/></svg>
        <span>18 Maple Row Lane, 2nd Floor,<br>Fairview, CT 06000</span>
      </li>
    </ul>

    <div class="brand">
      <div class="brand__mark" aria-hidden="true"></div>
      <div class="brand__name">RIDGELINE<br>CIVIL INC</div>
    </div>
  </article>
</body>
</html>
```